FIRE ALARM INSTALLATION & MAINTENANCE COMPANY NEEDS A BUSINESS CARD DESIGN

WE NEED A BUSINESS CARD DESIGN FOR AN EXISTING COMPANY IN QUEENSLAND AUSTRALIA. WE DESIGN & INSTALL FIRE DETECTION AND EMERGENCY WARNING SYSTEMS.
WE OFFER COMPREHENSIVE MAINTEANCE ON ALL FIRE PREVENTION SYSTEMS. OUR EXISTING LOGO IS ATTACHED. WE WOULD LIKE TO SEE A FRESH CREATIVE LOOK AND THINK THAT PERHAPS HAVING A BLACK OR SLATE BACKGROUND WILL ENHANCE THE COLOURS OF THE LOGO MORE. WE NEED PROVISION FOR NAMES, MOBILE PHONE NUMBERS AND WEB THE ADDRESS.

Target Market(s)

Australian Construction Project managers,construction business owners, building owners/managers, body corporate.

Industry/Entity Type

Business

Font styles to use
Serif
Sans Serif

Requirements
Must have
• Must use the logo.
On the back side of the card it needs to have:
Installation of: Fire Detection and Emergency Warning Systems
Comprehensive maintenance of all Fire Protection and prevention equipment and systems.
24/7 on call maintenance
Nice to have
• We think that use a black or slate background would make the logo standout more.
We dont mind if the wording TECHNOLOGIES AND Brindle Alarm & Egress under the logo is moved in order to center or balance the design layout.
Should not have
• no illustrations or motifs

```html
<!DOCTYPE html>
<html lang="en">
<head>
<meta charset="utf-8">
<title>Brindle Technologies – Business Card</title>
<link rel="stylesheet" href="https://fonts.googleapis.com/css2?family=Jost:wght@300;400;500&family=Archivo:wght@700;800&family=Oswald:wght@500&display=swap">
<style>
  :root {
    --backdrop: #3b3e43;
    --card: #131313;
    --orange: #f7941d;
    --blue: #343a9c;
    --brick: #a8343c;
    --white: #ffffff;
    --muted: #e9e9e9;
  }
  * { margin: 0; padding: 0; box-sizing: border-box; }
  html, body {
    width: 1037px; height: 1200px; overflow: hidden;
    background: var(--backdrop);
  }
  .sheet { position: relative; width: 1037px; height: 1200px; }
  .card {
    position: absolute; left: 187px; width: 704px; height: 399px;
    background: var(--card);
  }
  .card--front { top: 121px; }
  .card--back { top: 650px; }

  /* Front side: brand block */
  .brand-stack { position: absolute; left: 48px; top: 90px; width: 330px; }
  .brand-mark { display: flex; align-items: center; gap: 18px; }
  .brand-mark__dot { width: 74px; height: 74px; border-radius: 50%; background: var(--orange); flex: none; }
  .brand-mark__name {
    font-family: "Archivo", Arial, sans-serif; font-weight: 800;
    font-size: 58px; line-height: 1; color: var(--blue); letter-spacing: 1px;
  }
  .brand-stack__tech {
    margin-top: 44px;
    font-family: "Archivo", Arial, sans-serif; font-weight: 800;
    font-size: 27px; letter-spacing: 3.4px; color: var(--blue); line-height: 1;
  }
  .brand-stack__division {
    margin-top: 6px;
    font-family: "Archivo", Arial, sans-serif; font-weight: 700;
    font-size: 25px; color: var(--brick); line-height: 1;
  }

  /* Front side: services */
  .services {
    position: absolute; right: 35px; top: 96px; width: 300px;
    text-align: right; font-family: "Jost", sans-serif; font-weight: 400;
    font-size: 17.5px; line-height: 23px; color: var(--muted);
  }
  .services p + p { margin-top: 10px; }
  .services__callout {
    margin-top: 22px;
    font-family: "Oswald", sans-serif; font-weight: 500;
    font-size: 20px; letter-spacing: 0.3px; color: var(--orange);
  }

  /* Back side */
  .lockup { position: absolute; left: 46px; top: 60px; display: flex; align-items: center; gap: 22px; }
  .lockup__dot { width: 120px; height: 120px; border-radius: 50%; background: var(--orange); flex: none; }
  .lockup__text { font-family: "Archivo", Arial, sans-serif; line-height: 1; }
  .lockup__tech { font-weight: 800; font-size: 27px; letter-spacing: 3.6px; color: var(--white); }
  .lockup__division { margin-top: 5px; font-weight: 700; font-size: 24px; color: var(--orange); }

  .holder {
    position: absolute; left: 42px; top: 284px;
    font-family: "Jost", sans-serif; font-weight: 300;
    font-size: 33px; letter-spacing: 1.5px; color: var(--white);
  }
  .contact-list {
    position: absolute; left: 428px; top: 282px; list-style: none;
    font-family: "Jost", sans-serif; font-weight: 400; font-size: 20px; color: var(--orange);
  }
  .contact-list li { display: flex; align-items: center; gap: 8px; height: 28.5px; }
  .contact-list svg { width: 18px; height: 18px; flex: none; }
</style>
</head>
<body>
<main class="sheet">

  <section class="card card--front" aria-label="Card front">
    <div class="brand-stack">
      <div class="brand-mark">
        <span class="brand-mark__dot"></span>
        <span class="brand-mark__name">BRINDLE</span>
      </div>
      <div class="brand-stack__tech">TECHNOLOGIES</div>
      <div class="brand-stack__division">Brindle Alarm &amp; Egress</div>
    </div>

    <div class="services">
      <p>Installation of:</p>
      <p>Fire Detection and<br>Emergency Warning<br>Systems</p>
      <p>Comprehensive<br>maintenance of all Fire<br>Protection and prevention<br>equipment and systems.</p>
      <p class="services__callout">24/7 ON CALL MAINTENANCE</p>
    </div>
  </section>

  <section class="card card--back" aria-label="Card back">
    <div class="lockup">
      <span class="lockup__dot"></span>
      <div class="lockup__text">
        <div class="lockup__tech">BRINDLE TECHNOLOGIES</div>
        <div class="lockup__division">Brindle Alarm &amp; Egress</div>
      </div>
    </div>

    <div class="holder">DANA WHITLOW</div>

    <ul class="contact-list">
      <li>
        <svg viewBox="0 0 18 18" aria-hidden="true"><rect width="18" height="18" rx="4" fill="var(--orange)"/><rect x="6" y="3.5" width="6" height="11" rx="1.2" fill="none" stroke="#131313" stroke-width="1.4"/><circle cx="9" cy="12.3" r="0.8" fill="#131313"/></svg>
        000-000-0000
      </li>
      <li>
        <svg viewBox="0 0 18 18" aria-hidden="true"><rect width="18" height="18" rx="4" fill="var(--orange)"/><rect x="3.5" y="5" width="11" height="8" rx="1" fill="none" stroke="#131313" stroke-width="1.4"/><path d="M3.8 5.5 9 9.6l5.2-4.1" fill="none" stroke="#131313" stroke-width="1.3"/></svg>
        dw@brindletech.com
      </li>
      <li>
        <svg viewBox="0 0 18 18" aria-hidden="true"><rect width="18" height="18" rx="4" fill="var(--orange)"/><circle cx="9" cy="9" r="5.2" fill="none" stroke="#131313" stroke-width="1.3"/><ellipse cx="9" cy="9" rx="2.2" ry="5.2" fill="none" stroke="#131313" stroke-width="1.1"/><path d="M3.8 9h10.4" stroke="#131313" stroke-width="1.1"/></svg>
        www.brindletech.com
      </li>
    </ul>
  </section>

</main>
</body>
</html>
```